NEW YORK Plumbing/utility company 10 year anniversary business card

Looking For simple back and front business card would like to include a few things in description
We offer 24/7 emergency service
residential
commercial
industrial
municipal
services offered
Plumbing
hydro excavation
hydro jetting
Well pumps
Sewer pumps
water mains
sewer mains

```html
<!DOCTYPE html>
<html lang="en">
<head>
<meta charset="utf-8">
<title>Ridgeline Water &amp; Sewer – Business Card</title>
<link href="https://fonts.googleapis.com/css2?family=Arimo:wght@400;700&family=Montserrat:wght@600;800&display=swap" rel="stylesheet">
<style>
  :root {
    --backdrop: #1d1d1f;
    --navy: #0b3d7e;
    --navy-deep: #03275a;
    --blue-bright: #0a5a9a;
    --emboss: #0a2f66;
    --red: #d7262e;
    --paper: #f3f4f6;
    --grey-text: #5b5f66;
    --divider: #b9bcc2;
    --white: #ffffff;
  }
  * { box-sizing: border-box; margin: 0; padding: 0; }
  html, body { width: 1200px; height: 800px; overflow: hidden; }
  body {
    background: var(--backdrop);
    font-family: "Arimo", Arial, sans-serif;
    position: relative;
  }
  .card {
    position: absolute;
    left: 320px;
    width: 560px;
    height: 320px;
    overflow: hidden;
  }
  /* Back side */
  .card-back {
    top: 50px;
    background: linear-gradient(100deg, var(--navy-deep) 0%, var(--navy) 55%, var(--blue-bright) 100%);
  }
  .back-wordmark {
    position: absolute;
    top: 70px;
    left: 0; right: 0;
    text-align: center;
    font-family: "Montserrat", sans-serif;
    font-weight: 800;
    color: var(--emboss);
    line-height: 1.1;
  }
  .back-wordmark .name { font-size: 58px; letter-spacing: 3px; display: block; }
  .back-wordmark .sub { font-size: 22px; letter-spacing: 6px; display: block; }
  .service-list {
    position: absolute;
    bottom: 34px;
    left: 0; right: 0;
    text-align: center;
    color: var(--white);
    font-size: 14px;
    line-height: 1.55;
  }
  .service-list .dot { margin: 0 6px; }

  /* Front side */
  .card-front {
    top: 430px;
    background: var(--paper);
  }
  .front-brand {
    position: absolute;
    left: 36px;
    top: 78px;
    width: 230px;
    display: flex;
    align-items: center;
    gap: 10px;
  }
  .brand-dot {
    width: 22px; height: 22px;
    border-radius: 50%;
    background: var(--navy);
    flex: none;
  }
  .brand-name {
    font-family: "Montserrat", sans-serif;
    font-weight: 800;
    color: var(--navy);
    font-size: 27px;
    line-height: 1.05;
    letter-spacing: 1px;
  }
  .divider {
    position: absolute;
    left: 292px;
    top: 40px;
    width: 1px;
    height: 150px;
    background: var(--divider);
  }
  .contact {
    position: absolute;
    left: 316px;
    top: 44px;
  }
  .person-name {
    font-size: 24px;
    font-weight: 700;
    color: var(--navy);
  }
  .person-role {
    font-size: 13px;
    color: var(--grey-text);
    margin-top: 2px;
  }
  .contact-list {
    list-style: none;
    margin-top: 22px;
    font-size: 13px;
    color: var(--grey-text);
  }
  .contact-list li {
    display: flex;
    align-items: center;
    gap: 9px;
    margin-bottom: 6px;
  }
  .contact-list svg { width: 13px; height: 13px; flex: none; }
  .markets-band {
    position: absolute;
    left: 0; right: 0;
    top: 236px;
    height: 36px;
    background: var(--navy);
    color: var(--white);
    font-size: 14px;
    display: flex;
    align-items: center;
    padding-left: 110px;
    gap: 10px;
  }
  .markets-band .sep {
    width: 5px; height: 5px; border-radius: 50%;
    background: var(--white);
  }
  .service-tag {
    position: absolute;
    right: 28px;
    top: 222px;
    width: 68px;
    height: 52px;
    background: var(--red);
    border-radius: 4px;
    color: var(--white);
    text-align: center;
    font-family: "Montserrat", sans-serif;
    font-weight: 800;
    line-height: 1;
    padding-top: 9px;
  }
  .service-tag .hours { font-size: 19px; display: block; }
  .service-tag .label { font-size: 9px; letter-spacing: 1px; display: block; margin-top: 4px; }
</style>
</head>
<body>

<section class="card card-back" aria-label="Card back">
  <div class="back-wordmark">
    <span class="name">RIDGELINE</span>
    <span class="sub">WATER &amp; SEWER</span>
  </div>
  <div class="service-list">
    <p>Plumbing<span class="dot">•</span>Hydro excavation<span class="dot">•</span>Hydro jetting<span class="dot">•</span>Well pumps</p>
    <p>Sewer pumps<span class="dot">•</span>Water mains<span class="dot">•</span>Sewer mains</p>
  </div>
</section>

<section class="card card-front" aria-label="Card front">
  <div class="front-brand">
    <span class="brand-dot"></span>
    <span class="brand-name">RIDGELINE<br>WATER &amp; SEWER</span>
  </div>
  <div class="divider"></div>
  <div class="contact">
    <p class="person-name">Daniel Brooks</p>
    <p class="person-role">Managing Director</p>
    <ul class="contact-list">
      <li>
        <svg viewBox="0 0 24 24" aria-hidden="true"><path fill="#0b3d7e" d="M6.6 10.8a15 15 0 0 0 6.6 6.6l2.2-2.2c.3-.3.7-.4 1-.2 1.1.4 2.3.6 3.6.6.6 0 1 .4 1 1V20c0 .6-.4 1-1 1A17 17 0 0 1 3 4c0-.6.4-1 1-1h3.5c.6 0 1 .4 1 1 0 1.3.2 2.5.6 3.6.1.3 0 .7-.2 1z"/></svg>
        845-555-0192
      </li>
      <li>
        <svg viewBox="0 0 24 24" aria-hidden="true"><rect x="2" y="5" width="20" height="14" rx="1.5" fill="#0b3d7e"/><path d="M3 6l9 7 9-7" stroke="#fff" stroke-width="1.6" fill="none"/></svg>
        info@ridgelinews.com
      </li>
      <li>
        <svg viewBox="0 0 24 24" aria-hidden="true"><circle cx="12" cy="12" r="10" fill="#0b3d7e"/><path d="M2 12h20M12 2c3 3 3 17 0 20M12 2c-3 3-3 17 0 20" stroke="#fff" stroke-width="1.3" fill="none"/></svg>
        www.ridgelinews.com
      </li>
    </ul>
  </div>
  <div class="markets-band">
    <span>Residential</span><span class="sep"></span>
    <span>Commercial</span><span class="sep"></span>
    <span>Industrial</span><span class="sep"></span>
    <span>Municipal</span>
  </div>
  <div class="service-tag">
    <span class="hours">24/7</span>
    <span class="label">SERVICE</span>
  </div>
</section>

</body>
</html>
```